Packaging Design for Makeup Remover Pads - The winner will do several follow-up products with us

We are building a new brand (Ecological, Young, Friendly, Sustainable, High Quality). We are starting with Makeup Remover Pads. Once the product is launched, other products will follow. We would love to find a designer who does all follow-up designs for us. Our product contains 24 pads with 70% bamboo and 30% cotton. It has 3 layers as a highlight and a free washing bag made of 100% cotton. We would be really happy with a modern, high-quality design. You do not have to invent everything new. Please read the enclosed project description (.pdf file)

Target Market(s)

Women who think sustainably and ecologically

Logo Text

BRIMO TALVE

Colors

Designer to choose colors to be used in the design.

Requirements
Must have
• Our product is% 26quot; premium% 26quot ;. This should be written on the packaging and by a top design. 2 layers of cotton / bamboo. We have 3 layers in top quality. Our package contains 24 pieces, which is more than comparable products have. The whole design should immediately show the customer that it is a sustainable product. It would be great if the logo% 26quot; BRIMO TALVE% 26quot; what a combined word-picture logo. Our first idea is holding hands, or hugging, or holding hands in their hands or holding hands on the earth, or .... This is just to give you a rough idea. Feel free to come up with your own ideas.
Nice to have
• We uploaded a product with a cute panda on the package. An eye-catcher of that kind would be fabulous.

```html
<!DOCTYPE html>
<html lang="en">
<head>
<meta charset="utf-8">
<title>BRIMO TALVE – Reusable Make Up Remover Pads</title>
<link rel="stylesheet" href="https://fonts.googleapis.com/css2?family=Quicksand:wght@400;500;600;700&display=swap">
<style>
  :root {
    --backdrop: #f2f2f2;
    --kraft: #9a8672;
    --kraft-side: #8c7865;
    --ink-white: #f7f5f1;
    --lime: #b5e32a;
    --band-green: #7eb02c;
    --bamboo-dark: #3f5a1e;
    --bamboo-light: #7a8f45;
  }
  * { box-sizing: border-box; margin: 0; padding: 0; }
  html, body { width: 1200px; height: 900px; overflow: hidden; }
  body {
    background: var(--backdrop);
    font-family: "Quicksand", sans-serif;
    display: flex;
    align-items: center;
    justify-content: center;
  }
  .package { display: flex; height: 800px; }
  .side-panel {
    width: 230px;
    height: 100%;
    background: var(--kraft-side);
    position: relative;
  }
  .bamboo-art {
    position: absolute;
    inset: 30px 20px 20px 20px;
    background: linear-gradient(160deg, var(--bamboo-light) 0%, var(--bamboo-dark) 60%, rgba(63,90,30,0.35) 100%);
    border-radius: 4px;
  }
  .front-panel {
    width: 420px;
    height: 100%;
    background: var(--kraft);
    color: var(--ink-white);
    position: relative;
    display: flex;
    flex-direction: column;
    align-items: center;
  }
  .brand {
    margin-top: 90px;
    display: flex;
    flex-direction: column;
    align-items: center;
    gap: 22px;
  }
  .brand-dot {
    width: 64px; height: 64px;
    border-radius: 50%;
    background: var(--ink-white);
  }
  .brand-name {
    font-weight: 700;
    font-size: 44px;
    letter-spacing: 1px;
  }
  .count-block {
    margin-top: 110px;
    display: flex;
    align-items: center;
    gap: 18px;
    width: 360px;
  }
  .count {
    color: var(--lime);
    font-weight: 600;
    font-size: 96px;
    line-height: 1;
  }
  .count-desc {
    font-size: 20px;
    font-weight: 500;
    line-height: 1.2;
  }
  .divider {
    width: 360px;
    height: 2px;
    background: var(--ink-white);
    margin-top: 22px;
  }
  .product-type {
    width: 360px;
    margin-top: 18px;
    font-size: 20px;
    font-weight: 600;
  }
  .bag-note {
    width: 360px;
    margin-top: 4px;
    font-size: 16px;
    font-weight: 600;
  }
  .features {
    width: 360px;
    margin-top: 40px;
    display: flex;
    justify-content: space-between;
  }
  .feature {
    display: flex;
    flex-direction: column;
    align-items: center;
    gap: 12px;
    width: 110px;
  }
  .feature svg { width: 68px; height: 68px; }
  .feature-label { font-size: 11px; font-weight: 500; white-space: nowrap; }
  .claims-band {
    position: absolute;
    left: 0; right: 0; bottom: 70px;
    height: 56px;
    background: var(--band-green);
    display: flex;
    align-items: center;
    justify-content: center;
    font-size: 15px;
    font-weight: 700;
    white-space: nowrap;
  }
</style>
</head>
<body>
  <main class="package">
    <aside class="side-panel">
      <div class="bamboo-art" role="img" aria-label="Illustration of green bamboo stalks and leaves"></div>
    </aside>
    <section class="front-panel">
      <header class="brand">
        <span class="brand-dot"></span>
        <h1 class="brand-name">BRIMO TALVE</h1>
      </header>

      <div class="count-block">
        <span class="count">24</span>
        <p class="count-desc">premium natural<br>cotton &amp; bamboo<br>three layered pads</p>
      </div>
      <div class="divider"></div>
      <p class="product-type">reusable make up remover pads</p>
      <p class="bag-note">+ 1 wash bag made of 100% cotton</p>

      <ul class="features">
        <li class="feature">
          <svg viewBox="0 0 68 68" fill="none" stroke="#f7f5f1" stroke-width="1.6">
            <circle cx="34" cy="34" r="32"/>
            <circle cx="34" cy="30" r="8"/>
            <circle cx="26" cy="36" r="7"/>
            <circle cx="42" cy="36" r="7"/>
          </svg>
          <span class="feature-label">2 coton layers</span>
        </li>
        <li class="feature">
          <svg viewBox="0 0 68 68" fill="none" stroke="#f7f5f1" stroke-width="1.6">
            <circle cx="34" cy="34" r="32"/>
            <line x1="28" y1="16" x2="28" y2="52"/>
            <line x1="36" y1="16" x2="36" y2="52"/>
            <line x1="25" y1="28" x2="31" y2="28"/>
            <line x1="33" y1="38" x2="39" y2="38"/>
          </svg>
          <span class="feature-label">1 bamboo layer</span>
        </li>
        <li class="feature">
          <svg viewBox="0 0 68 68" fill="none" stroke="#f7f5f1" stroke-width="1.6">
            <circle cx="34" cy="34" r="32"/>
            <polyline points="14,30 10,34 14,38"/>
            <polyline points="54,30 58,34 54,38"/>
            <text x="34" y="34" fill="#f7f5f1" stroke="none" font-family="Quicksand, sans-serif" font-size="16" font-weight="700" text-anchor="middle">8</text>
            <text x="34" y="45" fill="#f7f5f1" stroke="none" font-family="Quicksand, sans-serif" font-size="9" text-anchor="middle">cm</text>
          </svg>
          <span class="feature-label">3 natural layers</span>
        </li>
      </ul>

      <div class="claims-band">vegan . sustainable . no chemicals . recyclable</div>
    </section>
  </main>
</body>
</html>
```